Apply color filter to a number of images to match a stylised existing design

I have an existing website design that I like. www.fernquilo.com. The blue pictures were all done previously and I do not have access to the people or process. Working on a new website and I need to process some screenshots in a similar stylised way. One test image is attached. The winning design/process will then process about 10 images for me.

```html
<!DOCTYPE html>
<html lang="en">
<head>
<meta charset="utf-8">
<title>FernquiloFly Live Video</title>
<link href="https://fonts.googleapis.com/css2?family=Roboto:wght@400;500&family=Open+Sans:wght@400;600&display=swap" rel="stylesheet">
<style>
  :root{
    --page:#ffffff;
    --water-deep:#1c4f93;
    --water-mid:#2a62a8;
    --shore:#6f93a8;
    --sand:#a9c2d0;
    --titlebar:#dcecf7;
    --ink:#1a2a6c;
    --menu-bg:#f1e6ee;
    --menu-ink:#1030b8;
    --green:#22e022;
    --hud:#eef4ff;
    --panel-bar:#f7e4ec;
    --panel-gray:#a7a3b3;
    --panel-pink:#ea5f88;
    --meas-bg:#0404a6;
    --meas-ink:#2f7bff;
    --yellow:#e8f55a;
    --dark-pill:#13284b;
    --dark-btn:#0c1a33;
  }
  *{box-sizing:border-box;margin:0;padding:0}
  html,body{width:1200px;height:800px;overflow:hidden;background:var(--page)}
  body{position:relative;font-family:"Roboto",sans-serif}
  .window{position:absolute;left:55px;top:93px;width:1090px;height:613px;background:var(--water-deep);overflow:hidden}
  .titlebar{position:absolute;left:0;top:0;width:100%;height:18px;background:var(--titlebar);display:flex;align-items:center;padding-left:6px;font:400 7px "Open Sans",sans-serif;color:var(--ink)}
  .titlebar .app-dot{width:8px;height:8px;background:#2a62c8;border-radius:50%;margin-right:6px}
  .titlebar .controls{position:absolute;right:10px;top:3px;display:flex;gap:18px;font-size:9px;color:#334}
  .scene{position:absolute;left:0;top:18px;width:100%;height:595px;
    background:linear-gradient(180deg,var(--water-mid) 0%,var(--water-deep) 55%,#2b5f96 70%,var(--shore) 80%,var(--sand) 92%,#93aebf 100%)}
  .menu{position:absolute;left:3px;width:113px;background:var(--menu-bg);font:600 9px "Open Sans",sans-serif;color:var(--menu-ink)}
  .menu .item{height:20px;display:flex;align-items:center;padding-left:4px;position:relative;border-bottom:1px solid #cfc3cc}
  .menu .item::after{content:"";position:absolute;right:0;top:0;width:21px;height:100%;background:var(--green)}
  .menu .dock{height:11px;background:#a9a5b3;font-size:6px;text-align:center;color:#223;line-height:11px}
  .hud{position:absolute;color:var(--hud);font-family:"Roboto",sans-serif;text-shadow:0 0 2px rgba(0,0,0,.35)}
  .mode{left:121px;top:40px;font-size:21px}
  .state{left:229px;top:40px;font-size:21px}
  .battery{position:absolute;left:725px;top:33px;width:37px;height:37px;border-radius:50%;border:2px solid #27c48a;color:#27c48a;font-size:13px;display:flex;align-items:center;justify-content:center}
  .timer{left:770px;top:37px;font-size:23px}
  .sats{left:980px;top:42px;font-size:16px}
  .more{left:1032px;top:36px;font-size:20px;letter-spacing:1px}
  .more b{color:#d8e83a;font-weight:500}
  .pill{position:absolute;left:930px;top:237px;width:60px;height:110px;border-radius:30px;background:var(--dark-pill)}
  .round{position:absolute;width:56px;height:56px;border-radius:50%;background:var(--dark-btn);color:var(--hud);display:flex;align-items:center;justify-content:center;font-size:19px}
  .shutter{position:absolute;left:1014px;top:294px;width:66px;height:66px;border-radius:50%;background:#e4e7ef}
  .panel{position:absolute}
  .panel .bar{height:21px;background:var(--panel-bar);position:relative;font:400 9px "Open Sans",sans-serif;color:var(--menu-ink);padding:5px 4px}
  .panel .bar::before{content:"";position:absolute;right:21px;top:0;width:21px;height:100%;background:var(--panel-gray)}
  .panel .bar::after{content:"";position:absolute;right:0;top:0;width:21px;height:100%;background:var(--panel-pink)}
  .measure{left:337px;top:413px;width:285px;height:162px}
  .measure .body{height:141px;background:var(--meas-bg);position:relative}
  .modes{position:absolute;left:5px;top:8px;width:147px;height:103px;border:1px solid #2a52d8;font:400 8.5px "Open Sans",sans-serif;color:var(--meas-ink);padding:14px 0 0 9px}
  .modes legend{position:absolute;top:-5px;left:6px;font-size:6px;background:var(--meas-bg);padding:0 2px}
  .modes li{list-style:none;height:23px;display:flex;align-items:center;gap:8px}
  .modes li::before{content:"";width:5px;height:5px;border-radius:50%;background:#fff}
  .modes li.on::before{background:#2f7bff}
  .readout{position:absolute;right:10px;color:var(--yellow);text-align:right;line-height:1}
  .r1{top:10px;font-size:35px}
  .r2{top:46px;font-size:35px}
  .r3{top:94px;right:3px;font-size:12px;display:flex;gap:16px;align-items:center}
  .r3 .tag{font-size:6px;color:var(--meas-ink);display:flex;gap:4px;align-items:center;margin-right:-8px}
  .r3 .tag::before{content:"";width:5px;height:5px;background:#fff}
  .r4{top:113px;right:3px;font-size:12px}
  .zoom{left:712px;top:352px;width:200px;height:240px}
  .zoom .view{height:202px;background:linear-gradient(180deg,#1f4f92,#1a4689)}
  .zoom .foot{height:17px;background:#f3eef3;display:flex;align-items:center;gap:20px;padding-left:6px;font:400 8px "Open Sans",sans-serif;color:#1a2a8c}
  .zoom .foot .live{font-size:5px}
  .bl{font-size:17px}
  .icon{position:absolute}
</style>
</head>
<body>
<div class="window">
  <div class="titlebar"><span class="app-dot"></span>FernquiloFly Live Video
    <span class="controls"><span>–</span><span>▢</span><span>✕</span></span>
  </div>
  <div class="scene" role="img" aria-label="Blue-tinted aerial view of a lake with lane lines, a floating swimmer, a pontoon and the shoreline with tents"></div>

  <div class="menu" style="top:23px">
    <div class="dock">Dock All</div>
    <div class="item">Setup</div>
    <div class="item">Settings</div>
    <div class="item">Drone</div>
  </div>
  <div class="menu" style="top:139px"><div class="item">Debug</div></div>

  <div class="hud mode">Mode</div>
  <div class="hud state">In flight</div>
  <div class="battery">73</div>
  <div class="hud timer">30'33"</div>
  <svg class="icon" style="left:853px;top:42px" width="100" height="22" viewBox="0 0 100 22" fill="none" stroke="#eef4ff" stroke-width="2">
    <path d="M2 18v-3M7 18v-6M12 18v-9M17 18v-12"/>
    <text x="22" y="16" fill="#eef4ff" stroke="none" font-size="10" font-family="Roboto,sans-serif">RC</text>
    <circle cx="60" cy="11" r="7"/><circle cx="60" cy="11" r="3"/>
    <path d="M73 4v9M73 16v2"/>
  </svg>
  <svg class="icon" style="left:962px;top:38px" width="18" height="22" viewBox="0 0 18 22" fill="none" stroke="#eef4ff" stroke-width="2"><path d="M3 15l6-6 4 4-6 6zM11 5l4 4M2 20c2 0 5-1 6-3"/></svg>
  <div class="hud sats">28</div>
  <div class="hud more">•••<b>H</b></div>

  <div class="pill"></div>
  <div class="round" style="left:932px;top:239px;width:56px;height:56px">3</div>
  <div class="round" style="left:932px;top:290px;color:var(--yellow)">1×</div>
  <div class="round" style="left:929px;top:353px;width:62px;height:62px;background:var(--dark-pill);font-weight:500">AF</div>
  <div class="shutter"></div>
  <svg class="icon" style="left:1035px;top:218px" width="26" height="20" viewBox="0 0 26 20" fill="none" stroke="#eef4ff" stroke-width="2"><rect x="1" y="1" width="24" height="18" rx="2"/><rect x="4" y="4" width="18" height="12"/></svg>
  <svg class="icon" style="left:1035px;top:414px" width="26" height="20" viewBox="0 0 26 20"><rect x="0" y="0" width="26" height="20" rx="2" fill="#eef4ff"/><path d="M10 5l8 5-8 5z" fill="#0c1a33"/></svg>

  <svg class="icon" style="left:18px;top:276px" width="30" height="28" viewBox="0 0 30 28" fill="none" stroke="#e0ee4a" stroke-width="2.5"><path d="M4 24c0-10 6-18 8-10s2 10 6 0 8-8 8 6"/></svg>
  <svg class="icon" style="left:18px;top:346px" width="30" height="36" viewBox="0 0 30 36" fill="none" stroke="#eef4ff" stroke-width="2"><path d="M15 4l-6 8h4v8h4v-8h4z" fill="#eef4ff"/><ellipse cx="15" cy="28" rx="12" ry="5"/></svg>

  <div class="panel measure">
    <div class="bar">Measurement</div>
    <div class="body">
      <ul class="modes"><legend>Measurement Mode</legend>
        <li>View</li><li class="on">Explore</li><li>Manual Measure</li><li>Auto Measure</li>
      </ul>
      <div class="readout r1">36.2</div>
      <div class="readout r2">119</div>
      <div class="readout r3"><span class="tag">MT15</span><span>33.835</span><span>4.600</span></div>
      <div class="readout r4">34146</div>
    </div>
  </div>

  <div class="hud" style="left:917px;top:574px;font-size:15px">Format&nbsp;&nbsp;EV</div>
  <div class="panel zoom">
    <div class="bar">Zoom</div>
    <div class="view" role="img" aria-label="Magnified blue-tinted view of a swimmer floating on the water"></div>
    <div class="foot"><span>◉ x 2</span><span>○ x 4</span><span>○ x 8</span><span class="live">Live Update ☐</span></div>
  </div>

  <div style="position:absolute;left:18px;top:562px;width:58px;height:51px;background:#3a8bd0" aria-hidden="true"></div>
  <svg class="icon" style="left:18px;top:562px" width="58" height="51" viewBox="0 0 58 51"><path d="M0 26L22 6M0 26l22 25" stroke="#dfe8f2" stroke-width="8" fill="none"/><path d="M40 16a8 8 0 0 1 16 0c0 7-8 15-8 15s-8-8-8-15z" fill="#f3c233"/><circle cx="48" cy="16" r="3" fill="#3a8bd0"/></svg>
  <div class="hud bl" style="left:118px;top:569px">0.0m/s</div>
  <div class="hud bl" style="left:220px;top:569px">0.0m/s</div>
  <div class="hud" style="left:92px;top:594px;font-size:20px">H&nbsp;60m</div>
  <div class="hud" style="left:195px;top:594px;font-size:20px">D&nbsp;182m</div>
  <div class="hud" style="left:813px;top:594px;font-size:20px">▪ 1185&nbsp;&nbsp;JPEG&nbsp;0.0</div>
  <svg class="icon" style="left:1033px;top:584px" width="32" height="24" viewBox="0 0 32 24" fill="none" stroke="#eef4ff" stroke-width="2"><rect x="1" y="4" width="30" height="19" rx="3"/><path d="M10 4l2-3h8l2 3"/><text x="5" y="18" fill="#eef4ff" stroke="none" font-size="8" font-family="Roboto,sans-serif">AUTO</text></svg>
</div>
</body>
</html>
```